LOS PINOS DE ARENA - EXCLUSIVE AND LUXURY REAL ESTATE PROJECT

Se trata del diseño de un mono poste grande (4 m x 2 m) o (8m x 3m) anunciando la construcción de 30 villas de lujo en un terreno en primera línea de playa en el sur de España (Cádiz).

La idea es crear expectación y transmitir lujo y exclusividad.

Target Market(s)

Clientes de alto poder adquisitivo que quieran adquirir su segunda vivienda en un entorno privilegiado a escasos pasos de una de las playas más bonitas de Cádiz.

Industry/Entity Type

REAL ESTATE

Colors

Designer to choose colors to be used in the design.

Requirements
Must have
• LOS PINOS DE ARENA as the name of the development
Nice to have
• Crear expectación con ideas del tipo: “Coming soon” o “No te lo puedes perder”

```html
<!DOCTYPE html>
<html lang="en">
<head>
<meta charset="UTF-8">
<title>Los Pinos de Arena – Coming Soon Billboard</title>
<link href="https://fonts.googleapis.com/css2?family=Oswald:wght@500;700&family=Kaushan+Script&display=swap" rel="stylesheet">
<style>
  :root {
    --navy: #0b1829;
    --orange: #f6a12c;
    --white: #ffffff;
    --stage: #e8e4e3;
    --sky-top: #3f6fc4;
    --sky-low: #9fc0e6;
    --facade: #e9e9e7;
    --terrace: #e7e2d8;
  }
  * { margin: 0; padding: 0; box-sizing: border-box; }
  html, body {
    width: 960px;
    height: 1200px;
    overflow: hidden;
    background: var(--stage);
  }
  .billboard {
    position: absolute;
    left: 60px;
    top: 390px;
    width: 840px;
    height: 420px;
    background: var(--navy);
    box-shadow: 0 6px 14px rgba(0, 0, 0, 0.25);
    overflow: hidden;
  }
  .title-panel {
    position: absolute;
    left: 210px;
    top: 0;
    right: 0;
    height: 168px;
    background: var(--white);
  }
  .hero-photo {
    position: absolute;
    left: 35px;
    top: 18px;
    width: 482px;
    height: 384px;
    background:
      linear-gradient(180deg, transparent 0%, transparent 60%, var(--terrace) 60%, #f1eee8 100%),
      linear-gradient(90deg, var(--sky-top) 0%, var(--sky-low) 16%, var(--facade) 24%, #d9d7d2 60%, #c9b99a 85%, #b8a888 100%);
  }
  .project-name {
    position: absolute;
    right: 40px;
    top: 14px;
    font-family: "Oswald", sans-serif;
    font-weight: 700;
    font-size: 58px;
    line-height: 64px;
    color: var(--navy);
    text-align: right;
  }
  .tagline-band {
    position: absolute;
    left: 517px;
    right: 0;
    top: 168px;
    height: 44px;
    background: var(--orange);
    display: flex;
    align-items: center;
    justify-content: center;
  }
  .tagline {
    font-family: "Oswald", sans-serif;
    font-weight: 700;
    font-size: 26px;
    line-height: 1;
    color: var(--navy);
  }
  .launch-message {
    position: absolute;
    left: 520px;
    right: 0;
    top: 248px;
    height: 150px;
  }
  .launch-coming {
    position: absolute;
    left: 0;
    right: 0;
    top: 0;
    text-align: center;
    font-family: "Oswald", sans-serif;
    font-weight: 700;
    font-size: 84px;
    line-height: 84px;
    color: var(--orange);
  }
  .launch-soon {
    position: absolute;
    left: 16px;
    right: 0;
    top: 35px;
    text-align: center;
    font-family: "Kaushan Script", cursive;
    font-size: 84px;
    line-height: 84px;
    color: var(--white);
  }
</style>
</head>
<body>
  <div class="billboard">
    <div class="title-panel"></div>
    <div class="hero-photo" role="img" aria-label="Photograph of a modern white two-storey luxury villa with wooden accents, large glass windows, a sunlit terrace with white lounge furniture and a blue sky"></div>
    <h1 class="project-name">LOS PINOS<br>DE ARENA</h1>
    <div class="tagline-band">
      <p class="tagline">You can't Miss it</p>
    </div>
    <div class="launch-message">
      <p class="launch-coming">COMING</p>
      <p class="launch-soon">Soon!</p>
    </div>
  </div>
</body>
</html>
```